Business Cards for wirefen.com.au
Logo already designed by Quillnoxa
Professional
Liam Forbury
Technical Engineer
Mobile: 0437 125 806
liam@wirefen.com.au
www.wirefen.com.au
Should have the text: "Cloud Application Development"

```html
<!DOCTYPE html>
<html lang="en">
<head>
<meta charset="utf-8">
<title>wirefen.com.au business card</title>
<link rel="stylesheet" href="https://fonts.googleapis.com/css2?family=Open+Sans:wght@400;600;700&display=swap">
<style>
  :root {
    --bg: #eceae6;
    --card: #ffffff;
    --brand-blue: #1f5ea8;
    --accent-blue: #2a6db5;
    --ink-grey: #4a4a4a;
    --soft-blue: #cfe0f0;
    --soft-blue-fade: #eef4fa;
  }
  * { margin: 0; padding: 0; box-sizing: border-box; }
  html, body {
    width: 1200px; height: 935px; overflow: hidden;
    background: var(--bg);
    font-family: "Open Sans", Arial, sans-serif;
  }
  .canvas {
    width: 1200px; height: 935px;
    display: flex; align-items: center; justify-content: center;
  }
  .business-card {
    position: relative;
    width: 1000px; height: 590px;
    background: var(--card);
    border-radius: 48px;
    overflow: hidden;
    box-shadow: 0 6px 24px rgba(0,0,0,0.12);
  }
  .side-decoration {
    position: absolute;
    left: -190px; top: 40px;
    width: 500px; height: 560px;
    border-radius: 50%;
    background: radial-gradient(circle at 60% 40%, var(--soft-blue) 0%, var(--soft-blue-fade) 60%, rgba(255,255,255,0) 75%);
    opacity: 0.8;
  }
  .person {
    position: absolute; left: 355px; top: 95px;
  }
  .person-name {
    color: var(--brand-blue);
    font-weight: 700; font-size: 38px; line-height: 1.1;
  }
  .person-title {
    color: var(--ink-grey);
    font-weight: 600; font-size: 21px; margin-top: 4px;
  }
  .divider {
    position: absolute; left: 352px; top: 200px;
    width: 4px; height: 290px;
    background: linear-gradient(var(--accent-blue), rgba(42,109,181,0.15));
  }
  .brand {
    position: absolute; left: 378px; top: 215px;
  }
  .brand-name {
    display: flex; align-items: center; gap: 14px;
    color: var(--ink-grey);
    font-weight: 700; font-size: 68px; line-height: 1; letter-spacing: -1px;
  }
  .brand-dot {
    width: 30px; height: 30px; border-radius: 50%;
    background: var(--accent-blue);
  }
  .brand-tagline {
    color: var(--accent-blue);
    font-weight: 400; font-size: 29px; margin-top: 10px;
  }
  .contact {
    position: absolute; left: 378px; top: 385px;
    font-size: 25px; line-height: 1.45; color: var(--ink-grey);
  }
  .contact-row { display: flex; gap: 8px; }
  .contact-label {
    color: var(--brand-blue); font-weight: 700;
    width: 104px; text-align: right;
  }
</style>
</head>
<body>
  <main class="canvas">
    <section class="business-card">
      <div class="side-decoration" role="img" aria-label="Faint pale blue brand decoration"></div>

      <div class="person">
        <p class="person-name">Liam Forbury</p>
        <p class="person-title">Technical Engineer</p>
      </div>

      <div class="divider"></div>

      <div class="brand">
        <p class="brand-name"><span class="brand-dot"></span>wirefen.com.au</p>
        <p class="brand-tagline">Cloud Application Development</p>
      </div>

      <div class="contact">
        <p class="contact-row"><span class="contact-label">Mobile :</span><span>0437 125 806</span></p>
        <p class="contact-row"><span class="contact-label">Email :</span><span>liam@wirefen.com.au</span></p>
        <p class="contact-row"><span class="contact-label">Web :</span><span>www.wirefen.com.au</span></p>
      </div>
    </section>
  </main>
</body>
</html>
```